Poster - Series of Poster Designs

We have a number of motivational quotes related to weight loss and fitness which need putting into a series of posters.
The designs need to:
- Reflect the current brand (see www.hillwardhavens.com.au)
- Be designed with scalability in mind to fit to A1, A3, A4, and A5. All portrait layout.
- Incorporate our logo
- Any images need to relfect the diversity of our clients ranging from 70kgs up to 200kgs.
- We have a stock of photos which can be used, or you can source your own (subject to budget approval)
Total of 26 posters in total, but all on the same design series (so effectively 1 design, with 26 applications).
The series of quotes are attached. An example quote would be:
-
"The difference between your body this week and next week is what you do for the next seven days to achieve your goals"
-
Our clients are a range of ages (20 - 60) and split male/female so colours should be neutral and reflect our orange/green branding. A modern feel but not super modern.
Output needs to be A3 ready to print with all source files included so that we can amend in the future.
There may be ongoing work for the right designer.

```html
<!DOCTYPE html>
<html lang="en">
<head>
<meta charset="utf-8">
<title>Hillward Havens – Motivation Poster</title>
<link rel="stylesheet" href="https://fonts.googleapis.com/css2?family=Oswald:wght@400;500;600&display=swap">
<style>
  :root {
    --brand-orange: #f39a17;
    --brand-orange-dark: #c97806;
    --brand-green: #80bc26;
    --brand-green-dark: #5d8e16;
    --ink-grey: #4b4b4b;
    --ring-border: #4a4a4a;
    --paper: #ffffff;
    --paper-shade: #ececec;
  }
  * { margin: 0; padding: 0; box-sizing: border-box; }
  html, body { width: 905px; height: 1200px; overflow: hidden; }
  body {
    position: relative;
    background: linear-gradient(180deg, var(--paper) 0%, var(--paper) 60%, var(--paper-shade) 100%);
    font-family: "Oswald", "Arial Narrow", sans-serif;
  }
  .progress-ring {
    position: absolute;
    left: 112px;
    top: 14px;
    width: 680px;
    height: 680px;
  }
  .ring-shadow {
    position: absolute;
    left: 276px;
    top: 736px;
    width: 353px;
    height: 18px;
    border-radius: 50%;
    background: radial-gradient(ellipse at center, rgba(0,0,0,0.35) 0%, rgba(0,0,0,0.12) 45%, rgba(0,0,0,0) 72%);
  }
  .quote {
    position: absolute;
    left: 189px;
    top: 796px;
    width: 545px;
    transform: rotate(-4deg);
    transform-origin: center;
    text-align: center;
    text-transform: uppercase;
    line-height: 1;
  }
  .quote-line {
    display: block;
    color: var(--ink-grey);
    font-weight: 500;
    font-size: 28px;
    letter-spacing: 0.2px;
    padding: 4px 0 5px;
  }
  .quote-band {
    position: relative;
    display: block;
    color: var(--paper);
    font-weight: 500;
    font-size: 47px;
    padding: 4px 10px 6px;
    margin-right: 14px;
  }
  .quote-band::after {
    content: "";
    position: absolute;
    right: -14px;
    top: -10px;
    width: 14px;
    height: calc(100% + 10px);
    clip-path: polygon(0 10px, 100% 0, 100% calc(100% - 10px), 0 100%);
  }
  .quote-band--orange { background: var(--brand-orange); }
  .quote-band--orange::after { background: var(--brand-orange-dark); }
  .quote-band--green { background: var(--brand-green); }
  .quote-band--green::after { background: var(--brand-green-dark); }
  .brand {
    position: absolute;
    left: 0;
    width: 905px;
    top: 1098px;
    display: flex;
    justify-content: center;
    align-items: center;
    gap: 12px;
  }
  .brand-mark {
    width: 46px;
    height: 46px;
    border-radius: 50%;
    background: var(--brand-orange);
  }
  .brand-text { display: flex; flex-direction: column; align-items: flex-end; }
  .brand-name {
    color: var(--brand-green);
    font-weight: 600;
    font-size: 40px;
    line-height: 1;
    letter-spacing: 0.5px;
    text-transform: uppercase;
  }
  .brand-tagline {
    color: var(--ink-grey);
    font-weight: 500;
    font-size: 13px;
    letter-spacing: 0.4px;
    text-transform: uppercase;
    margin-top: 2px;
  }
</style>
</head>
<body>
  <svg class="progress-ring" viewBox="0 0 680 680" xmlns="http://www.w3.org/2000/svg">
    <defs>
      <radialGradient id="runner-photo-tone" cx="55%" cy="45%" r="65%">
        <stop offset="0%" stop-color="#e6ddd2"/>
        <stop offset="40%" stop-color="#9c8f86"/>
        <stop offset="80%" stop-color="#5a5552"/>
        <stop offset="100%" stop-color="#3c3a39"/>
      </radialGradient>
    </defs>
    <path class="ring-segment ring-segment--orange" fill="var(--brand-orange)"
          d="M598.2 123.4 A337 337 0 1 1 81.8 123.4 L340 340 Z"/>
    <path class="ring-segment ring-segment--green" fill="var(--brand-green)"
          d="M81.8 123.4 A337 337 0 0 1 598.2 123.4 L340 340 Z"/>
    <circle class="ring-hole-border" cx="340" cy="340" r="214" fill="var(--ring-border)"/>
    <g role="img" aria-label="Photo of a runner's legs and trainers on an open road under a stormy sky">
      <circle class="ring-photo" cx="340" cy="340" r="207" fill="url(#runner-photo-tone)"/>
    </g>
  </svg>

  <div class="ring-shadow"></div>

  <p class="quote">
    <span class="quote-line">The difference between your body</span>
    <span class="quote-band quote-band--orange">This week and next week</span>
    <span class="quote-line">Is what you do for the next seven days</span>
    <span class="quote-band quote-band--green">To achieve your goals</span>
  </p>

  <div class="brand">
    <span class="brand-mark"></span>
    <span class="brand-text">
      <span class="brand-name">Hillward Havens</span>
      <span class="brand-tagline">Weight Loss Retreat</span>
    </span>
  </div>
</body>
</html>
```